Staffing/Recruitment company

We need to upgrade our website. At the moment we have a template that was built last year and looks not good at all.
We would like to update it with a new design based on what is popular this year. Including some visual effects etc.
This website is to give all information to our potential clients about what we do, clients with worked in the past, how to contact us and about us.
The website consists of 4 pages.
We would like to see a design that uses the color blue.
The current website is https://brightkelvo.us/
Logo of the company is uploaded

Some designs were not complete...

```html
<!DOCTYPE html>
<html lang="en">
<head>
<meta charset="utf-8">
<title>Bright Kelvo – Staffing &amp; Recruitment</title>
<link href="https://fonts.googleapis.com/css2?family=Questrial&family=Open+Sans:wght@400;600;700&display=swap" rel="stylesheet">
<style>
:root{
  --navy:#0b0c4f;
  --navy-dark:#07083a;
  --orange:#f26a21;
  --blue:#2d7fe8;
  --text:#4a4a55;
  --muted:#8a8a96;
  --line:#e3e4ea;
  --hero-a:#f4f3ee;
  --hero-b:#e9e7df;
  --green-a:#e4f0d9;
  --green-b:#cfe5bf;
  --partner-bg:#eef1f8;
  --footer:#1c1e24;
  --footer-dark:#15161b;
  --white:#ffffff;
}
*{box-sizing:border-box;margin:0;padding:0}
html,body{width:1200px;height:3591px;overflow:hidden}
body{font-family:"Open Sans",sans-serif;color:var(--text);background:var(--white);position:relative;font-size:11px;line-height:1.7}
.abs{position:absolute}
h1,h2,h3,.display{font-family:"Questrial",sans-serif;font-weight:400}
.ph{display:block}
.btn{display:inline-block;font-family:"Open Sans",sans-serif;font-weight:700;font-size:10px;letter-spacing:.8px;text-transform:uppercase;padding:0 22px;line-height:28px}
.circle{border-radius:50%}

/* top bar */
.topbar{left:0;top:0;width:1200px;height:45px;background:var(--navy)}
.topbar .contact{left:234px;top:0;line-height:45px;color:#d5d6ea;font-size:10px;display:flex;gap:40px}
.topbar .contact span::before{content:"";display:inline-block;width:7px;height:7px;border-radius:50%;background:var(--orange);margin-right:7px;vertical-align:middle}
.topbar .social{right:231px;top:12px;display:flex;gap:8px}
.topbar .social i{width:20px;height:20px;border-radius:50%;background:var(--blue);display:block}
.topbar .social i:nth-child(2),.topbar .social i:nth-child(3){background:var(--orange)}

/* header */
.header{left:0;top:45px;width:1200px;height:55px;background:var(--white);border-bottom:1px solid var(--line)}
.brand{display:flex;align-items:center;gap:9px;font-family:"Questrial",sans-serif;font-size:17px;font-weight:400;color:var(--navy);letter-spacing:.5px}
.brand i{width:20px;height:20px;background:var(--orange);display:block}
.header .brand{left:234px;top:16px}
.nav{right:230px;top:0;display:flex;align-items:center;gap:30px;height:55px;font-size:10px;font-weight:600;color:var(--navy);text-transform:uppercase}
.nav .active{color:var(--orange)}
.nav .search{width:26px;height:26px;border-radius:50%;background:var(--orange);display:flex;align-items:center;justify-content:center}

/* hero */
.hero{left:0;top:100px;width:1200px;height:555px;background:linear-gradient(90deg,var(--hero-a),var(--hero-b))}
.hero h1{left:234px;top:168px;font-size:34px;color:var(--navy)}
.hero h1 em{font-style:normal;color:var(--orange)}
.hero p{left:234px;top:218px;width:440px;font-size:11px;color:var(--text)}
.hero .btn{left:234px;top:302px;background:var(--orange);color:var(--white)}
.hero .person{left:655px;top:0;width:340px;height:555px;background:linear-gradient(180deg,#cfcbc2,#a9a59c)}
.hero .dots{left:1160px;top:196px;display:flex;flex-direction:column;gap:10px;align-items:center;font-size:8px;color:var(--muted)}
.hero .dots b{width:6px;height:6px;border-radius:50%;background:var(--navy);display:block}

/* divisions */
.section-title{width:1200px;left:0;text-align:center;font-size:28px;color:var(--navy);letter-spacing:1px}
.divisions{top:697px}
.division{top:760px;width:220px;text-align:center}
.division .icon{width:58px;height:58px;margin:0 auto;border-radius:50%;background:var(--white);box-shadow:0 3px 12px rgba(0,0,0,.12);position:relative;display:flex;align-items:center;justify-content:center}
.division .icon::before{content:"";position:absolute;top:-6px;left:21px;width:16px;height:16px;border-radius:50%;background:var(--navy)}
.division h3{margin-top:18px;font-size:13px;color:var(--navy);text-transform:uppercase}
.division.featured h3{color:var(--orange)}
.division p{margin-top:8px;font-size:10px;color:var(--muted);line-height:1.75}
.division .more{margin-top:4px;font-size:9px;color:var(--orange);font-weight:600}

/* team + about */
.team{left:300px;top:1062px;width:540px;height:210px;background:linear-gradient(180deg,#f1f1f3,#c9cbd3)}
.about{left:234px;top:1270px;width:735px;height:360px;background:var(--navy);text-align:center;color:var(--white)}
.about .brand{justify-content:center;color:var(--white);margin-top:52px;font-size:17px}
.about .brand i{background:var(--white)}
.about h2{margin-top:18px;font-size:25px;letter-spacing:.5px}
.about p{width:560px;margin:20px auto 0;font-size:10px;color:#c8c9e4;line-height:1.8}
.about .btn{margin-top:26px;background:var(--white);color:var(--navy)}

/* services */
.services{top:1708px}
.tabs{left:234px;top:1797px;width:150px}
.tabs li{list-style:none;display:flex;justify-content:space-between;align-items:center;height:33px;font-size:10px;color:var(--text)}
.tabs li::after{content:"";width:10px;height:10px;border-radius:50%;border:1px solid #b9bac8}
.tabs li.active{color:var(--orange);font-weight:700}
.tabs li.active::after{background:var(--navy);border-color:var(--navy)}
.service-body{left:424px;top:1797px;width:330px}
.service-body h3{font-family:"Open Sans",sans-serif;font-size:11px;font-weight:700;color:var(--orange)}
.service-body p{margin-top:10px;font-size:9.5px;color:var(--muted);line-height:1.75}
.service-body ul{margin-top:12px;display:grid;grid-template-columns:1fr 1fr;row-gap:6px}
.service-body li{list-style:none;font-size:9.5px;color:var(--text);display:flex;align-items:center;gap:10px}
.service-body li::before{content:"";width:10px;height:10px;border-radius:50%;background:var(--navy)}
.service-image{left:795px;top:1797px;width:174px;height:168px;background:linear-gradient(180deg,#e9e9ee,#b9bccb);border:2px solid var(--navy)}

/* network band */
.network{left:0;top:2046px;width:1200px;height:309px;background:linear-gradient(90deg,var(--green-a),var(--green-b))}
.network .geek{left:655px;top:0;width:340px;height:309px;background:linear-gradient(180deg,#c3d4b8,#8fa6a0)}
.network h2{left:250px;top:60px;font-size:33px;color:var(--navy)}
.network .sub{left:250px;top:108px;font-family:"Questrial",sans-serif;font-size:19px;color:var(--navy)}
.network .call{left:250px;top:142px;font-size:12px;color:var(--navy)}
.network .call b{color:var(--orange);font-weight:600;font-size:14px}
.network .btn{left:390px;top:196px;background:var(--navy);color:var(--white)}

/* news */
.news-kicker{left:0;width:1200px;top:2424px;text-align:center;font-size:10px;color:var(--muted)}
.news-kicker b{color:var(--orange);font-weight:600}
.news-title{top:2446px;font-size:20px}
.card{top:2538px;width:232px;height:327px;background:var(--white);box-shadow:0 4px 18px rgba(0,0,0,.10)}
.card .thumb{width:232px;height:177px;position:relative}
.card .date{position:absolute;right:14px;bottom:-20px;width:40px;height:40px;border-radius:50%;background:var(--orange);color:var(--white);text-align:center;font-size:8px;font-weight:700;line-height:1.15;padding-top:9px}
.card.alt .date{background:var(--navy)}
.card .meta{margin:26px 18px 0;font-size:8px;color:var(--muted);display:flex;gap:16px}
.card h3{margin:6px 18px 0;font-family:"Open Sans",sans-serif;font-size:12px;font-weight:600;color:var(--navy)}
.card p{margin:8px 18px 0;font-size:9px;color:var(--muted);line-height:1.7}
.card .read{margin:12px 18px 0;font-size:9px;font-weight:700;color:var(--orange)}

/* partners */
.partners{left:0;top:2955px;width:1200px;height:225px;background:var(--partner-bg)}
.partner{top:75px;width:114px;height:75px;background:var(--white);box-shadow:0 2px 8px rgba(0,0,0,.06);display:flex;align-items:center;justify-content:center}
.partner i{display:block;width:44px;height:22px;border-radius:4px;background:#c7cad6}
.partner.round i{width:36px;height:36px;border-radius:50%}
.partner.bordered{outline:2px solid #d4d6e0}

/* footer */
.footer{left:0;top:3180px;width:1200px;height:360px;background:var(--footer);color:#a8a9b3}
.footer .up{left:584px;top:-16px;width:32px;height:32px;border-radius:50%;background:var(--orange);display:flex;align-items:center;justify-content:center}
.footer .col{top:78px}
.footer .brand{color:var(--white);font-size:15px}
.footer .brand i{background:var(--white);width:18px;height:18px}
.footer h4{font-family:"Open Sans",sans-serif;font-size:11px;font-weight:700;color:var(--white);text-transform:uppercase;letter-spacing:.5px}
.footer .about-text{margin-top:20px;width:150px;font-size:9px;line-height:1.7}
.footer .contacts{margin-top:14px;font-size:9px;list-style:none}
.footer .contacts li{display:flex;align-items:center;gap:9px;height:22px}
.footer .contacts li::before{content:"";width:8px;height:8px;border-radius:50%;background:#d0d1d8}
.footer .links{margin-top:30px;list-style:none;font-size:9px}
.footer .links li{height:20px}
.footer .links li::before{content:"› ";color:var(--orange)}
.gallery{margin-top:42px;display:grid;grid-template-columns:repeat(4,48px);gap:2px;background:var(--footer)}
.gallery i{display:block;width:48px;height:48px;background:var(--white)}
.gallery i.hl{background:var(--blue)}
.footer .sub-label{margin-top:30px;font-size:9px}
.footer .field{margin-top:8px;width:170px;height:28px;background:#2b2d35;border:1px solid #3a3c46;font-size:9px;line-height:26px;padding:0 10px;color:#8b8c96;position:relative}
.footer .field::after{content:"";position:absolute;right:8px;top:9px;width:9px;height:9px;background:var(--white);border-radius:2px}
.footer .social{margin-top:22px;display:flex;gap:7px}
.footer .social i{display:block;width:18px;height:18px;border-radius:50%;background:#3a3c46}
.footer .social i:nth-child(2),.footer .social i:nth-child(3){background:var(--blue)}
.copyright{left:0;top:3540px;width:1200px;height:51px;background:var(--footer-dark);text-align:center;line-height:51px;font-size:9px;color:#7b7c86}
</style>
</head>
<body>

<div class="topbar abs">
  <div class="contact abs"><span>(800) 123-4567</span><span>info@brightkelvo.us</span></div>
  <div class="social abs"><i></i><i></i><i></i><i></i><i></i><i></i></div>
</div>

<header class="header abs">
  <div class="brand abs"><i></i>BRIGHT KELVO</div>
  <nav class="nav abs">
    <span class="active">Home</span><span>Clients</span><span>About Us</span><span>Contact</span>
    <span class="search"><svg width="11" height="11" viewBox="0 0 12 12"><circle cx="5" cy="5" r="3.6" fill="none" stroke="#fff" stroke-width="1.6"/><line x1="7.7" y1="7.7" x2="11" y2="11" stroke="#fff" stroke-width="1.6"/></svg></span>
  </nav>
</header>

<section class="hero abs">
  <div class="person abs ph" role="img" aria-label="Smiling businessman in a grey suit, hands on hips"></div>
  <div class="dots abs"><span>01</span><b></b><span>02</span><span>03</span><span>04</span></div>
</section>
<h1 class="abs" style="left:234px;top:268px;font-size:34px;color:var(--navy)">Join Our <span style="color:var(--orange)">Career Network</span></h1>
<p class="abs" style="left:234px;top:318px;width:440px;font-size:11px">Our Career Network will enhance your job search and application process. Whether you choose to apply or just leave your information, we look forward to staying connected with you.</p>
<a class="btn abs" style="left:234px;top:404px;background:var(--orange);color:var(--white)">Join</a>

<h2 class="section-title divisions abs">OUR DIVISIONS</h2>
<div class="division abs" style="left:194px">
  <div class="icon"><svg width="24" height="22" viewBox="0 0 24 22"><rect x="2" y="12" width="4" height="8" fill="#f26a21"/><rect x="9" y="7" width="4" height="13" fill="#f26a21"/><rect x="16" y="2" width="4" height="18" fill="#f26a21"/></svg></div>
  <h3>Finance</h3>
  <p>With Wall Street's fast-paced markets and ever-changing environment, finance teams are always searching for new skills and top talent to lead them.</p>
  <div class="more">Read More</div>
</div>
<div class="division abs featured" style="left:490px">
  <div class="icon"><svg width="26" height="22" viewBox="0 0 26 22"><rect x="2" y="2" width="22" height="14" rx="1" fill="none" stroke="#2d7fe8" stroke-width="2"/><rect x="9" y="17" width="8" height="3" fill="#2d7fe8"/></svg></div>
  <h3>Information Technology</h3>
  <p>The technology of today is not going to be the technology of tomorrow, and keeping up with the current innovation and change would be a full time job, so our team is ready to help you.</p>
  <div class="more">Read More</div>
</div>
<div class="division abs" style="left:786px">
  <div class="icon"><svg width="22" height="22" viewBox="0 0 22 22"><path d="M8 2h6v6h6v6h-6v6H8v-6H2V8h6z" fill="none" stroke="#f26a21" stroke-width="2"/></svg></div>
  <h3>Health Care</h3>
  <p>Not only do we provide services in the finance and technology world, we also service the healthcare industry with professionals who care.</p>
  <div class="more">Read More</div>
</div>

<div class="team abs ph" role="img" aria-label="Group of smiling business professionals standing together"></div>
<section class="about abs">
  <div class="brand"><i></i>BRIGHT KELVO</div>
  <h2>A BIT ABOUT BRIGHT KELVO, LLC</h2>
  <p>Over 10 and a half years we have grown from a startup company. Throughout the time we've built relationships, we've grown together internally and externally, and have created a system that allows us to get ever closer to the needs of our clients and candidates. We've been a reliable partner, a trusted builder for others, but most importantly we've been there for you, ready to help you navigate through the ever changing job market.</p>
  <a class="btn">Explore More</a>
</section>

<h2 class="section-title services abs">OUR SERVICES</h2>
<ul class="tabs abs">
  <li>Hire The Professional Staff</li>
  <li>Automation Of Infrastructure</li>
  <li class="active">Beyond Recruiting</li>
  <li>Subject Title 1</li>
  <li>Subject Title 2</li>
  <li>Subject Title 3</li>
</ul>
<div class="service-body abs">
  <h3>Beyond Recruiting for your team</h3>
  <p>We are committed to helping companies find the best talent, advanced partner network and teams working to connect companies with top talent. Our deep experience lets us guide you through sourcing, assessment and placement, so the right people join at the right time.</p>
  <ul>
    <li>Legal</li><li>Sales</li>
    <li>Internet</li><li>Mobile</li>
    <li>Consultant</li><li>Finance</li>
    <li>Tourism</li><li>Reporting Tools</li>
  </ul>
</div>
<div class="service-image abs ph" role="img" aria-label="Businessman surrounded by light bulb idea illustrations"></div>

<section class="network abs">
  <div class="geek abs ph" role="img" aria-label="Smiling support technician wearing a headset"></div>
  <h2 class="abs">Need a Network Geek?</h2>
  <div class="sub abs">We have newest technology innovations.</div>
  <div class="call abs">Call Now <b>(800) 123-4567</b> and let us craft a problem together!</div>
  <a class="btn abs">Booking Now</a>
</section>

<div class="news-kicker abs">From <b>The Blog</b></div>
<h2 class="section-title news-title abs">LATEST NEWS</h2>
<article class="card abs" style="left:234px">
  <div class="thumb"><div class="ph" role="img" aria-label="Man in a hat looking out over a valley" style="width:232px;height:177px;background:linear-gradient(180deg,#c7d3dc,#6f7f86)"></div><div class="date">26<br>JUN</div></div>
  <div class="meta"><span>By Admin</span><span>0 Comments</span></div>
  <h3>Donec venenatis turpis</h3>
  <p>We ensure new hire organization they deserve a huge amount of grants and members they highlight.</p>
  <div class="read">Reading...</div>
</article>
<article class="card abs alt" style="left:486px">
  <div class="thumb"><div class="ph" role="img" aria-label="Hand reaching toward a cloud network graphic" style="width:232px;height:177px;background:linear-gradient(180deg,#6e8fb5,#24345e)"></div><div class="date">26<br>JUN</div></div>
  <div class="meta"><span>By Admin</span><span>0 Comments</span></div>
  <h3>Donec venenatis turpis</h3>
  <p>We ensure new hire organization they deserve a huge amount of grants and members they highlight.</p>
  <div class="read">Reading...</div>
</article>
<article class="card abs alt" style="left:738px">
  <div class="thumb"><div class="ph" role="img" aria-label="Business colleagues meeting in a bright office" style="width:232px;height:177px;background:linear-gradient(180deg,#dfe6ee,#9fb0c2)"></div><div class="date">26<br>JUN</div></div>
  <div class="meta"><span>By Admin</span><span>0 Comments</span></div>
  <h3>Donec venenatis turpis</h3>
  <p>We ensure new hire organization they deserve a huge amount of grants and members they highlight.</p>
  <div class="read">Reading...</div>
</article>

<section class="partners abs">
  <div class="partner abs" style="left:237px"><i></i></div>
  <div class="partner abs" style="left:390px"><i></i></div>
  <div class="partner abs bordered" style="left:543px"><i></i></div>
  <div class="partner abs" style="left:696px"><i></i></div>
  <div class="partner abs round" style="left:849px"><i></i></div>
</section>

<footer class="footer abs">
  <div class="up abs"><svg width="12" height="12" viewBox="0 0 12 12"><path d="M2 8l4-4 4 4" fill="none" stroke="#fff" stroke-width="2"/></svg></div>
  <div class="col abs" style="left:234px">
    <div class="brand"><i></i>BRIGHT KELVO</div>
    <p class="about-text">We are staffing specialists connecting great talent with companies that need them, across finance, technology and health care.</p>
    <ul class="contacts">
      <li>(800) 123-4567</li>
      <li>info@brightkelvo.us</li>
      <li>2400 Main St, Suite 110</li>
    </ul>
  </div>
  <div class="col abs" style="left:420px">
    <h4>Useful Links</h4>
    <ul class="links"><li>Home</li><li>About Us</li><li>Clients</li><li>Contact Us</li></ul>
  </div>
  <div class="col abs" style="left:612px">
    <h4>Gallery</h4>
    <div class="gallery"><i></i><i class="hl"></i><i></i><i></i><i></i><i></i><i></i><i></i><i></i><i></i><i></i><i></i></div>
  </div>
  <div class="col abs" style="left:798px">
    <h4>Subscribe</h4>
    <div class="sub-label">Subscribe to the newsletter</div>
    <div class="field">Your email here</div>
    <div class="social"><i></i><i></i><i></i><i></i><i></i><i></i></div>
  </div>
</footer>
<div class="copyright abs">© 2021 Copyright Bright Kelvo, LLC All Rights Reserved</div>

</body>
</html>
```